Website - Tides Of Bloom

We are catalysts of change in people's lives.
We work with individuals and professionals to bring about instant substantial & transforming change in their lives.
We provide one-on-one lifestyle coaching by an experienced practitioner.
Our existing website is www.tidesofbloom.biz & this site contains our the basis for the content of our desired new project, so please examine this carefully.
We require a professional and captivating website that will instantly impress, engage invite our readers to click & invest their lives.
Our services do not come cheap, but are second to none.
Our website must be contemporary whilst reflecting indisputable class & ultra-confidence in the success of our work.
Target Market(s)
Those who seek to want to change in their lives. Those aged primarily between 30 and 50 years of age, male or female.
Industry/Entity Type
Work
Look and feel

```html
<!DOCTYPE html>
<html lang="en">
<head>
<meta charset="utf-8">
<title>Tides Of Bloom — About us</title>
<link rel="stylesheet" href="https://fonts.googleapis.com/css2?family=Open+Sans:ital,wght@0,300;0,400;0,600;0,700;1,400&family=Roboto+Condensed:wght@300;400;700&display=swap">
<style>
  :root {
    --page: #ffffff;
    --panel: #0c0c0c;
    --panel-edge: #050505;
    --lime: #8cc63f;
    --lime-dark: #5d8f1f;
    --text: #ffffff;
    --text-soft: #d6d6d6;
    --caption-bg: rgba(240, 240, 232, 0.88);
    --caption-text: #3a3a3a;
    --magenta: #e0144f;
    --orange: #e8702a;
    --blue: #1a9ad6;
  }
  * { margin: 0; padding: 0; box-sizing: border-box; }
  html, body { width: 1200px; height: 1000px; overflow: hidden; background: var(--page); }
  body { position: relative; font-family: "Open Sans", Arial, sans-serif; color: var(--text); }

  .site {
    position: absolute; left: 0; top: 93px; width: 1200px; height: 812px;
    background: radial-gradient(ellipse at 50% 35%, #1c1c1c 0%, var(--panel) 60%, var(--panel-edge) 100%);
    border-top: 7px solid var(--lime);
    border-bottom: 7px solid var(--lime);
    overflow: hidden;
  }
  .site__rail { position: absolute; right: 0; top: 0; width: 94px; height: 100%; background: #050505; }
  .swoosh { position: absolute; left: 0; top: 0; pointer-events: none; }

  .sound-toggle { position: absolute; left: 100px; top: 0; width: 20px; height: 20px; background: var(--lime); }
  .sound-toggle svg { display: block; }

  .brand { position: absolute; left: 806px; top: 40px; display: flex; align-items: center; gap: 14px; }
  .brand__dot { width: 52px; height: 52px; border-radius: 50%; background: var(--lime); }
  .brand__name { font-size: 27px; font-weight: 600; color: #c8c8c8; line-height: 1; }

  .section-title { position: absolute; left: 149px; top: 157px; width: 908px; height: 34px; border-bottom: 1px solid var(--lime); display: flex; align-items: center; }
  .section-title__mark { width: 23px; height: 34px; background: var(--lime); margin-right: 8px; }
  .section-title h1 { font-size: 23px; font-weight: 300; }
  .section-title h1 strong { font-weight: 600; }

  .intro { position: absolute; left: 149px; top: 212px; font-size: 12.5px; color: var(--text-soft); }

  .slider { position: absolute; left: 149px; top: 248px; width: 908px; height: 379px; }
  .slider__photo { position: absolute; inset: 0;
    background: linear-gradient(180deg, #2d4a6b 0%, #6f8fae 30%, #dfe6ec 62%, #f4efe0 75%, #5d6470 85%, #262a30 100%); }
  .slider__caption { position: absolute; left: 57px; top: 132px; width: 369px; height: 161px; background: var(--caption-bg); padding: 16px 38px; color: var(--caption-text); }
  .slider__caption h2 { font-family: "Roboto Condensed", Arial, sans-serif; font-size: 29px; font-weight: 300; line-height: 1; letter-spacing: 0.3px; }
  .slider__caption h2 strong { font-weight: 700; }
  .slider__caption p { font-family: "Roboto Condensed", Arial, sans-serif; font-size: 13.5px; line-height: 13px; font-weight: 300; }
  .slider__button { display: inline-block; margin-top: 10px; background: var(--lime); color: #fff; font-family: "Roboto Condensed", Arial, sans-serif; font-weight: 300; font-size: 18px; padding: 4px 19px; }
  .slider__tagline { margin-top: 9px; font-style: italic; font-size: 13.5px; }
  .slider__arrow { position: absolute; top: 169px; width: 41px; height: 41px; background: var(--lime); display: flex; align-items: center; justify-content: center; }
  .slider__arrow--prev { left: 0; opacity: 0.35; }
  .slider__arrow--next { right: 0; }
  .slider__dots { position: absolute; left: 590px; top: 640px; display: flex; gap: 17px; }
  .slider__dots span { width: 10px; height: 10px; border-radius: 50%; border: 1px solid #888; }
  .slider__dots span.is-active { background: #fff; border-color: #fff; box-shadow: 0 0 6px #fff; }

  .services { position: absolute; top: 692px; left: 149px; display: flex; }
  .service { position: relative; width: 309px; padding-left: 72px; font-size: 12px; line-height: 18px; color: var(--text-soft); }
  .service svg { position: absolute; left: 0; top: 4px; }
  .service h3 { font-size: 21px; font-weight: 700; color: var(--text); line-height: 24px; margin-bottom: 2px; }
  .service p { max-width: 215px; }
  .service p.wrap { margin-left: -72px; max-width: none; white-space: nowrap; }

  .pager { position: absolute; left: 38px; top: 760px; font-size: 31px; font-weight: 700; line-height: 1; }
  .pager span { color: var(--orange); }

  .menu-tab { position: absolute; left: 10px; top: 355px; transform: rotate(-90deg); transform-origin: left top; translate: 0 85px; font-size: 25px; font-weight: 400; letter-spacing: 0.5px; display: flex; align-items: center; gap: 4px; }
  .menu-tab::before { content: ""; width: 8px; height: 24px; background: var(--lime); }

  .fullscreen-toggle { position: absolute; left: 1088px; top: 778px; width: 18px; height: 18px; background: var(--lime); }
</style>
</head>
<body>
<main class="site">
  <div class="site__rail"></div>

  <svg class="swoosh" width="1200" height="812" viewBox="0 0 1200 812">
    <path d="M650 250 C720 120 800 40 930 0 L980 0 C850 50 760 140 690 250 Z" fill="#6aa62a" opacity="0.55"/>
    <path d="M760 120 C820 60 880 20 1000 0 L1106 0 L1106 30 C980 40 880 80 790 140 Z" fill="#7bbd32" opacity="0.75"/>
    <path d="M1106 40 C1140 20 1170 10 1200 0 L1200 30 C1170 40 1140 55 1106 70 Z" fill="#8cc63f"/>
    <path d="M0 620 C50 590 100 560 150 540 L150 560 C100 585 50 615 0 650 Z" fill="#8cc63f"/>
    <path d="M0 700 C50 660 100 620 150 595 L150 640 C100 665 50 700 0 745 Z" fill="#6aa62a"/>
    <path d="M0 770 C40 740 80 715 120 700 L120 712 C80 730 40 755 0 790 Z" fill="#8cc63f" opacity="0.8"/>
  </svg>

  <div class="sound-toggle">
    <svg width="20" height="20" viewBox="0 0 20 20"><path d="M5 8h3l4-3v10l-4-3H5z" fill="#fff"/><path d="M14 7.5q2 2.5 0 5" stroke="#fff" stroke-width="1.4" fill="none"/></svg>
  </div>

  <div class="brand">
    <span class="brand__dot"></span>
    <span class="brand__name">Tides Of Bloom</span>
  </div>

  <header class="section-title">
    <span class="section-title__mark"></span>
    <h1><strong>About us</strong> // Yes we can.</h1>
  </header>

  <p class="intro">At Tides Of Bloom, our Master Practitioner will inspire you, shifting your perspective &amp; facilitating your mind with the freedom to realise your dreams.</p>

  <section class="slider">
    <div class="slider__photo" role="img" aria-label="Photo: a man with arms raised facing a bright sky over the sea at sunrise"></div>
    <div class="slider__caption">
      <h2><strong>RESPONSIVE</strong>BEHAVIOR</h2>
      <p>Whether you're displaying on desktops, tablet, mobiles, your images, your products will always look the same!</p>
      <span class="slider__button">Read more...</span>
      <p class="slider__tagline">Make the best of it!</p>
    </div>
    <span class="slider__arrow slider__arrow--prev"><svg width="12" height="18" viewBox="0 0 12 18"><path d="M9 2 2 9l7 7" stroke="#fff" stroke-width="1.5" fill="none"/></svg></span>
    <span class="slider__arrow slider__arrow--next"><svg width="12" height="18" viewBox="0 0 12 18"><path d="M3 2l7 7-7 7" stroke="#fff" stroke-width="1.5" fill="none"/></svg></span>
  </section>
  <div class="slider__dots"><span class="is-active"></span><span></span><span></span></div>

  <section class="services">
    <article class="service">
      <svg width="62" height="62" viewBox="0 0 62 62"><rect x="2" y="2" width="34" height="34" fill="none" stroke="var(--magenta)" stroke-width="5"/><path d="M40 26h20v34H26V40" fill="none" stroke="var(--magenta)" stroke-width="5"/></svg>
      <h3>Business</h3>
      <p>Tides Of Bloom have worked with CEO's &amp; business owners throughout Australia, as catalysts to their</p>
      <p class="wrap">outstanding success. We will facilitate &amp; oversee</p>
    </article>
    <article class="service">
      <svg width="62" height="62" viewBox="0 0 62 62"><g fill="var(--orange)"><rect x="25" y="0" width="12" height="62"/><rect x="0" y="25" width="62" height="12"/><rect x="12" y="0" width="4" height="10"/><rect x="46" y="0" width="4" height="10"/><rect x="12" y="52" width="4" height="10"/><rect x="46" y="52" width="4" height="10"/><circle cx="31" cy="31" r="21"/></g><circle cx="31" cy="31" r="13" fill="#111"/><circle cx="31" cy="31" r="7" fill="var(--orange)"/></svg>
      <h3>Individual</h3>
      <p>Tides Of Bloom works every day with people just like you who wish to change their lives.</p>
      <p class="wrap">Mum's &amp; Dads experiencing marriage problems or</p>
    </article>
    <article class="service">
      <svg width="62" height="62" viewBox="0 0 62 62"><circle cx="31" cy="31" r="28" fill="none" stroke="var(--blue)" stroke-width="4"/><path d="M22 16c3-2 6 0 7 4s-2 5-2 7 3 8 6 10 4-1 6-1 5 3 4 6-4 5-7 4C26 42 18 30 22 16z" fill="var(--blue)"/></svg>
      <h3>Contact</h3>
      <p>We're so excited by it &amp; think its extraordinary! You've waited long enough...</p>
      <p class="wrap">If you want change, call Reid today on:</p>
    </article>
  </section>

  <div class="pager">01/<span>01</span></div>
  <div class="menu-tab">menu</div>
  <div class="fullscreen-toggle"><svg width="18" height="18" viewBox="0 0 18 18"><rect x="3" y="6" width="9" height="9" fill="none" stroke="#fff" stroke-width="1.4"/><path d="M8 3h7v7" fill="none" stroke="#fff" stroke-width="1.4"/></svg></div>
</main>
</body>
</html>
```